Carpentry and Building Business Card

I'm looking for a business card that is minimalistic and that incorporates the theme of my Velmi logo.
On one side I'd like the VELMI logo with my details on the other side.
Double sided with curved edges

Target Market(s)

Construction / renovation
Adults

Industry/Entity Type

Tradesman

Contact Information for Business Card

Logo on one side, details on the other

Colors

Designer to choose only greyscale colors for use in the design.

Requirements
Must have
• Niko Barlettis
VELMI CONSTRUCT
Carpentry & Building Services
0412385726
Velmiconstruct@brindlemail.com
Lic No. 618243D
Nice to have
• Fb and insta icons. @velmiconstruct
Should not have
• No hammer or tool icons please.

No address line.

```html
<!DOCTYPE html>
<html lang="en">
<head>
<meta charset="utf-8">
<title>Velmi Construct – Business Card</title>
<link rel="stylesheet" href="https://fonts.googleapis.com/css2?family=Montserrat:wght@400;500&family=Open+Sans:wght@400;600;700&display=swap">
<style>
  :root {
    --backdrop: #7a5a3a;
    --card-white: #fbfbfa;
    --card-grey: #ececec;
    --accent: #d4863a;
    --ink: #2a2a2a;
    --ink-soft: #3b3b3b;
    --on-accent: #fdf3e8;
  }
  html, body {
    margin: 0;
    padding: 0;
    width: 1200px;
    height: 1023px;
    overflow: hidden;
    background: var(--backdrop);
  }
  .canvas {
    position: relative;
    width: 1200px;
    height: 1023px;
  }
  .card {
    position: absolute;
    width: 540px;
    height: 310px;
    border-radius: 28px;
    overflow: hidden;
    box-shadow: 0 10px 24px rgba(0,0,0,0.35);
  }

  /* Front: wordmark */
  .card-front {
    left: 60px;
    top: 130px;
    background: var(--card-white);
    display: flex;
    align-items: center;
    justify-content: center;
    gap: 22px;
  }
  .brand-square {
    width: 46px;
    height: 46px;
    background: var(--accent);
  }
  .wordmark {
    font-family: "Montserrat", sans-serif;
    font-weight: 400;
    font-size: 64px;
    letter-spacing: 14px;
    color: var(--ink);
  }

  /* Back: details */
  .card-back {
    left: 600px;
    top: 560px;
    background: var(--card-grey);
    font-family: "Open Sans", sans-serif;
  }
  .back-top {
    position: absolute;
    left: 0; top: 0; right: 0;
    height: 180px;
    display: flex;
    align-items: center;
    justify-content: space-between;
    padding: 0 34px;
  }
  .back-brand {
    display: flex;
    align-items: center;
    gap: 14px;
  }
  .back-brand .brand-square { width: 34px; height: 34px; }
  .back-brand .brand-name {
    font-family: "Montserrat", sans-serif;
    font-weight: 500;
    font-size: 40px;
    letter-spacing: 8px;
    color: var(--accent);
  }
  .identity { text-align: left; }
  .person-name {
    margin: 0 0 8px;
    font-weight: 700;
    font-size: 21px;
    letter-spacing: 1.5px;
    color: var(--accent);
  }
  .company-name {
    margin: 0;
    font-weight: 700;
    font-size: 14px;
    letter-spacing: 0.5px;
    color: var(--ink);
  }
  .company-line {
    margin: 2px 0 0;
    font-size: 13px;
    color: var(--ink-soft);
  }
  .back-band {
    position: absolute;
    left: 0; right: 0; bottom: 0;
    height: 130px;
    background: var(--accent);
    padding: 24px 34px;
    box-sizing: border-box;
  }
  .contact-list {
    list-style: none;
    margin: 0;
    padding: 0;
    color: var(--on-accent);
    font-size: 15px;
    line-height: 27px;
  }
  .contact-label { margin-right: 6px; }
  .social-mark {
    display: inline-block;
    width: 13px;
    height: 13px;
    background: var(--on-accent);
    border-radius: 3px;
    margin-right: 8px;
    vertical-align: -1px;
  }
</style>
</head>
<body>
<main class="canvas">
  <section class="card card-front" aria-label="Card front">
    <span class="brand-square" aria-hidden="true"></span>
    <span class="wordmark">VELMI.</span>
  </section>

  <section class="card card-back" aria-label="Card back">
    <div class="back-top">
      <div class="back-brand">
        <span class="brand-square" aria-hidden="true"></span>
        <span class="brand-name">VELMI</span>
      </div>
      <div class="identity">
        <p class="person-name">NIKO BARLETTIS</p>
        <p class="company-name">VELMI CONSTRUCT</p>
        <p class="company-line">Carpentry &amp; Building Services</p>
        <p class="company-line">Lic No. 618243D</p>
      </div>
    </div>
    <div class="back-band">
      <ul class="contact-list">
        <li><span class="contact-label">[M]</span>0412385726</li>
        <li><span class="contact-label">[E]</span>Velmiconstruct@brindlemail.com</li>
        <li><span class="social-mark" aria-hidden="true"></span>@velmiconstruct</li>
      </ul>
    </div>
  </section>
</main>
</body>
</html>
```